Simple and creative Business Card

I have logo already. Would like a simple and creative design with no color [url removed, login to view] design have to be good looking. The logo can be 3D or 2D. Business card can be 1 sided or 2 sided that is better.

Details of the card:

Name : SK. TANVIR HOSSEN
Title : Director,Lumora Tutorial Coaching Centre.
Address : Tesora, Binnapur, Khulna.
Email : norvik47@[url removed, login to view]
Phone Number : +880 1555 019384
Facebook : [url removed, login to view]
Use my attached logo below.....

```html
<!DOCTYPE html>
<html lang="en">
<head>
<meta charset="utf-8">
<title>SK. Tanvir Hossen – Business Card</title>
<link rel="stylesheet" href="https://fonts.googleapis.com/css2?family=Arimo:wght@400;700&display=swap">
<style>
  :root {
    --bg: #3a3b3e;
    --card: #ffffff;
    --green: #2fb06a;
    --sky: #34a9e0;
    --navy: #2b3a9c;
    --ink: #2a3590;
    --shadow: rgba(0,0,0,0.35);
  }
  * { margin: 0; padding: 0; box-sizing: border-box; }
  html, body { width: 1200px; height: 900px; overflow: hidden; }
  body {
    background: var(--bg);
    font-family: "Arimo", Arial, sans-serif;
    position: relative;
  }
  .card {
    position: absolute;
    top: 295px;
    width: 540px;
    height: 310px;
    background: var(--card);
    box-shadow: 0 10px 24px var(--shadow);
    overflow: hidden;
  }
  .card--contact { left: 45px; }
  .card--brand { left: 615px; }

  /* Brand name block (stands where the mark sits) */
  .brand {
    position: absolute;
    display: flex;
    flex-direction: column;
    align-items: center;
    gap: 12px;
  }
  .brand__dot {
    width: 70px; height: 70px;
    border-radius: 50%;
    background: var(--sky);
  }
  .brand__name {
    font-size: 21px;
    font-weight: 400;
    color: var(--green);
    letter-spacing: 0.5px;
    white-space: nowrap;
  }
  .card--contact .brand { left: 22px; top: 80px; }
  .card--brand .brand { left: 50%; top: 46px; transform: translateX(-50%); }

  /* Puzzle pieces column */
  .pieces {
    position: absolute;
    left: 238px; top: 60px;
    width: 56px; height: 200px;
  }
  .piece {
    position: absolute;
    width: 40px; height: 40px;
    border-radius: 4px;
  }
  .piece--navy { background: var(--navy); left: 16px; top: 0; }
  .piece--sky { background: var(--sky); left: 4px; top: 72px; }
  .piece--green { background: var(--green); left: 12px; top: 146px; }

  /* Contact details */
  .details {
    position: absolute;
    left: 312px; top: 44px;
    color: var(--ink);
  }
  .details__name {
    font-size: 19px;
    font-weight: 400;
    letter-spacing: 0.3px;
    margin-bottom: 6px;
  }
  .details__title {
    font-size: 12.5px;
    line-height: 1.35;
    margin-bottom: 16px;
  }
  .details__list { list-style: none; }
  .details__item {
    display: flex;
    align-items: center;
    gap: 10px;
    font-size: 13px;
    height: 30px;
  }
  .details__icon {
    width: 20px; height: 20px;
    border-radius: 50%;
    background: var(--sky);
    flex: none;
  }

  /* Colour tabs on brand side */
  .tab { position: absolute; border-radius: 6px; }
  .tab--green { background: var(--green); left: -8px; top: 180px; width: 96px; height: 32px; }
  .tab--sky { background: var(--sky); left: 170px; top: 248px; width: 168px; height: 80px; }
  .tab--navy { background: var(--navy); left: 420px; top: 276px; width: 140px; height: 50px; }
</style>
</head>
<body>

<section class="card card--contact">
  <div class="brand">
    <span class="brand__dot"></span>
    <span class="brand__name">SK. TANVIR HOSSEN</span>
  </div>

  <div class="pieces" role="img" aria-label="Three puzzle pieces in navy, sky blue and green">
    <span class="piece piece--navy"></span>
    <span class="piece piece--sky"></span>
    <span class="piece piece--green"></span>
  </div>

  <div class="details">
    <h1 class="details__name">SK. TANVIR HOSSEN</h1>
    <p class="details__title">Director, Lumora Tutorial<br>Coaching Centre.</p>
    <ul class="details__list">
      <li class="details__item">
        <svg class="details__icon" viewBox="0 0 20 20"><circle cx="10" cy="10" r="10" fill="#34a9e0"/><path d="M10 4.5a3.5 3.5 0 0 0-3.5 3.5c0 2.6 3.5 6.5 3.5 6.5s3.5-3.9 3.5-6.5A3.5 3.5 0 0 0 10 4.5z" fill="#fff"/><circle cx="10" cy="8" r="1.3" fill="#34a9e0"/></svg>
        Tesora, Binnapur, Khulna.
      </li>
      <li class="details__item">
        <svg class="details__icon" viewBox="0 0 20 20"><circle cx="10" cy="10" r="10" fill="#34a9e0"/><rect x="5" y="6.5" width="10" height="7" fill="#fff"/><path d="M5 6.5l5 4 5-4" fill="none" stroke="#34a9e0" stroke-width="1"/></svg>
        norvik47@mailhaven.com
      </li>
      <li class="details__item">
        <svg class="details__icon" viewBox="0 0 20 20"><circle cx="10" cy="10" r="10" fill="#34a9e0"/><path d="M7 5.5c.6-.4 1.2 0 1.5.6l.7 1.5c.2.5 0 1-.4 1.3l-.6.4c.5 1.1 1.4 2 2.5 2.5l.4-.6c.3-.4.8-.6 1.3-.4l1.5.7c.6.3 1 .9.6 1.5-.7 1.1-2 1.6-3.3 1-2.2-1-3.9-2.7-4.9-4.9-.6-1.3-.1-2.6 1-3.3z" fill="#fff"/></svg>
        +880 1555 019384
      </li>
      <li class="details__item">
        <svg class="details__icon" viewBox="0 0 20 20"><circle cx="10" cy="10" r="10" fill="#34a9e0"/><circle cx="10" cy="10" r="5" fill="none" stroke="#fff" stroke-width="1.2"/><path d="M5 10h10M10 5c-2 2.8-2 7.2 0 10M10 5c2 2.8 2 7.2 0 10" fill="none" stroke="#fff" stroke-width="1"/></svg>
        www.lumoratutor.com
      </li>
    </ul>
  </div>
</section>

<section class="card card--brand">
  <div class="brand">
    <span class="brand__dot"></span>
    <span class="brand__name">SK. TANVIR HOSSEN</span>
  </div>
  <span class="tab tab--green"></span>
  <span class="tab tab--sky"></span>
  <span class="tab tab--navy"></span>
</section>

</body>
</html>
```